Gutschein-Design für Online-Yoga
Zielgruppe
Yogalehrerin sucht neue Kunden für Online Yoga.
Aufgabenstellung
Der Gutschein sollte im Postkartenformat für die Schweiz sein, damit dieser wieder zurückgeschickt werden kann.
Der Gutschein sollte ansprechend für die folgenden 5 YOGA-Zielgruppen sein: Kinder, Schwangere, Erwachsene, Senioren und Therapeutisch. Es soll ersichtlich sein, wie einfach es ist Online Yoga über die Webseite www.atemfluss.ch zu buchen und welchen nutzen die Kunden daraus haben Yoga Online zu machen. Eine kurze Vorstellung der Yogalehrerin Henrike Bolt (Bild beigefügt) sollte auch mit auf dem Gutschein stehen, sowie eine gute preisliche Aktionsauflage.
Das Logo ist ebenfalls hier zum download. Die folgenden Bilder können auch für den Gutschein verwendet werden:
https://www.bildkiste-demo.com/de/sammlung/tafeln/Qw8rTn3VbX5kLm2pYc7dHs

```html
<!DOCTYPE html>
<html lang="de">
<head>
<meta charset="utf-8">
<title>Atemfluss – Gutschein Online Yoga</title>
<link href="https://fonts.googleapis.com/css2?family=Crimson+Pro:wght@400;600;700&family=Yanone+Kaffeesatz:wght@300;400&family=Arimo&display=swap" rel="stylesheet">
<style>
  :root{
    --orange:#f07d1a;
    --red:#e8553a;
    --yellow:#f6b313;
    --peach:#fdf1e8;
    --ink:#333333;
    --line:#6d6d6d;
    --arc:#d8d8d8;
    --page:#ffffff;
  }
  *{box-sizing:border-box;margin:0;padding:0}
  html,body{width:1200px;height:848px;overflow:hidden;background:var(--page)}
  .sheet{position:relative;width:1200px;height:848px}
  .card{position:absolute;width:636px;height:450px;background:#fff;transform:scale(.896);transform-origin:0 0;
        box-shadow:0 1px 5px rgba(0,0,0,.35);overflow:hidden;font-family:"Crimson Pro",serif;color:var(--ink)}
  .card--front{left:20px;top:222px}
  .card--back{left:610px;top:222px}
  .card svg.art{position:absolute;left:0;top:0}
  .abs{position:absolute}

  /* front */
  .brand-box{left:35px;top:0;width:135px;height:85px;background:#fff;display:flex;align-items:center;justify-content:center;gap:7px}
  .brand-box .dot{width:12px;height:12px;border-radius:50%;background:var(--orange)}
  .brand-name{font-family:"Crimson Pro",serif;font-size:19px;font-weight:400;color:var(--orange);letter-spacing:.5px}
  .promo{left:472px;top:38px;width:126px;transform:rotate(-5deg);text-align:center;color:#fff;font-family:"Yanone Kaffeesatz",sans-serif;line-height:1}
  .promo b{display:block;font-weight:400;font-size:25px}
  .promo span{display:block;font-weight:300;font-size:16px}
  .headline{left:33px;top:190px;font-size:68px;font-weight:700;line-height:1;letter-spacing:-1px;
            background:linear-gradient(90deg,var(--orange),var(--red));-webkit-background-clip:text;background-clip:text;color:transparent}
  .subline{left:34px;top:259px;font-size:20px;font-weight:700;color:var(--orange)}
  .intro{left:34px;top:303px;width:360px;font-size:13.4px;line-height:18.5px}
  .intro a{color:var(--orange);font-weight:700;text-decoration:none}
  .steps{left:34px;top:401px;font-family:"Yanone Kaffeesatz",sans-serif;font-weight:300;font-size:19px}
  .steps i{font-style:normal;color:var(--orange);margin:0 6px}
  .group{font-family:"Yanone Kaffeesatz",sans-serif;font-weight:300;font-size:14px;color:var(--ink)}
  .courses{left:528px;top:300px;display:flex;align-items:center;gap:5px;font-size:12px;color:var(--orange)}
  .courses .dot{width:10px;height:10px;border-radius:50%;background:var(--orange)}

  /* back */
  .slogan{left:35px;top:26px;font-family:"Yanone Kaffeesatz",sans-serif;font-weight:300;font-size:18px}
  .code{left:35px;top:57px;width:128px;height:50px;background:#fff;display:flex;align-items:center;justify-content:center;
        font-family:"Yanone Kaffeesatz",sans-serif;font-weight:300;font-size:27px;color:var(--orange)}
  .terms{left:35px;top:118px;font-size:7.6px;line-height:10px}
  .teacher-name{left:145px;top:206px;font-size:13px;font-weight:700;color:var(--orange);letter-spacing:.3px}
  .teacher-role{left:145px;top:221px;font-size:10px}
  .field{position:absolute;left:35px;width:287px;border-bottom:1px solid var(--line);font-size:9.5px;height:14px}
  .field span{position:absolute;left:0;top:0}
  .field span + span{left:150px}
  .divider{left:336px;top:120px;width:2px;height:267px;background:var(--line)}
  .stamp{left:530px;top:35px;width:71px;height:84px;border:2px solid var(--ink);display:flex;align-items:center;justify-content:center;
         text-align:center;font-family:"Arimo",sans-serif;font-size:8.5px;line-height:10px}
  .address{left:392px;top:256px;font-family:"Arimo",sans-serif;font-size:15px;line-height:20px}
</style>
</head>
<body>
<main class="sheet">

  <!-- Vorderseite -->
  <section class="card card--front">
    <svg class="art" width="636" height="450" viewBox="0 0 636 450">
      <defs>
        <linearGradient id="photoTone" x1="0" y1="0" x2="1" y2="1">
          <stop offset="0" stop-color="#e9e4dc"/>
          <stop offset=".5" stop-color="#c9bfb2"/>
          <stop offset="1" stop-color="#8f8a84"/>
        </linearGradient>
        <linearGradient id="swoosh" x1="0" x2="1">
          <stop offset="0" stop-color="#f6b313"/>
          <stop offset=".6" stop-color="#f07d1a"/>
          <stop offset="1" stop-color="#e8553a"/>
        </linearGradient>
      </defs>
      <path role="img" aria-label="Foto: Frau dehnt sich auf der Yogamatte vor einem Laptop"
            d="M0 0H636V92C520 140 380 200 240 196C140 193 60 180 0 172Z" fill="url(#photoTone)"/>
      <path d="M0 172C60 180 140 193 240 196C380 200 520 140 636 92V106C520 156 380 212 240 208C140 206 60 192 0 186Z" fill="url(#swoosh)"/>
      <path d="M636 150C520 150 430 210 433 275C436 345 520 400 636 395" fill="none" stroke="var(--arc)" stroke-width="1.5"/>
      <ellipse cx="537" cy="76" rx="64" ry="41" fill="none" stroke="var(--orange)" stroke-width="2" transform="rotate(-6 537 76)"/>
      <ellipse cx="533" cy="80" rx="62" ry="40" fill="var(--yellow)" transform="rotate(-6 533 80)"/>
      <circle role="img" aria-label="Foto: Babybauch einer Schwangeren" cx="508" cy="162" r="30" fill="#e8d2bf"/>
      <circle role="img" aria-label="Foto: Mann in Meditationshaltung" cx="455" cy="208" r="30" fill="#b08a6c"/>
      <circle role="img" aria-label="Foto: Kinder beim Yoga" cx="435" cy="275" r="30" fill="#d9d6d2"/>
      <circle role="img" aria-label="Foto: Seniorin beim Yoga" cx="455" cy="341" r="30" fill="#9fb2bf"/>
      <circle role="img" aria-label="Foto: therapeutische Behandlung" cx="508" cy="390" r="30" fill="#ead7c8"/>
    </svg>

    <div class="abs brand-box"><span class="dot"></span><span class="brand-name">ATEMFLUSS</span></div>
    <div class="abs promo"><b>Aktionscode</b><span>auf der Rückseite</span></div>

    <span class="abs group" style="left:546px;top:154px">Schwangere</span>
    <span class="abs group" style="left:491px;top:200px">Erwachsene</span>
    <span class="abs group" style="left:471px;top:267px">Kinder</span>
    <span class="abs group" style="left:491px;top:326px">Senioren</span>
    <span class="abs group" style="left:545px;top:383px">Therapie</span>
    <div class="abs courses"><span class="dot"></span>YOGA KURSE</div>

    <h1 class="abs headline">Gutschein</h1>
    <p class="abs subline">GRATIS Probestunde Online Yoga</p>
    <p class="abs intro">Du suchst Entspannung im Alltag oder willst einfach fit werden? ATEMFLUSS ist dein persönliches Online-Yoga-Studio. Hier kannst du ganz bequem Yoga üben – wann und wo immer du willst. Probiere es doch gleich aus: <a href="#">www.atemfluss.ch</a></p>
    <p class="abs steps">Anmelden<i>»</i>Code eingeben<i>»</i>gratis Probestunde geniessen</p>
  </section>

  <!-- Rückseite -->
  <section class="card card--back">
    <svg class="art" width="636" height="450" viewBox="0 0 636 450">
      <defs>
        <linearGradient id="swoosh2" x1="0" x2="1">
          <stop offset="0" stop-color="#f6b313"/>
          <stop offset=".6" stop-color="#f07d1a"/>
          <stop offset="1" stop-color="#e8553a"/>
        </linearGradient>
      </defs>
      <path d="M0 0H325V160C240 175 110 185 0 148Z" fill="var(--peach)"/>
      <path d="M0 148C110 185 240 175 325 160V166C240 186 110 196 0 160Z" fill="url(#swoosh2)"/>
      <rect role="img" aria-label="Grafik: Laptop, Tablet und Smartphone" x="200" y="58" width="82" height="50" rx="3" fill="#e4e1de"/>
      <circle role="img" aria-label="Porträtfoto der Yogalehrerin" cx="83" cy="205" r="50" fill="#b9a58f"/>
    </svg>

    <p class="abs slogan">Zeit für Dich – zu Hause oder Unterwegs</p>
    <div class="abs code">CODEXY21</div>
    <p class="abs terms">Dieser Gutschein ist einmalig einlösbar bis xxx auf www.atemfluss.ch.<br>Nicht kumulierbar mit anderen Aktionen und Gutscheinen.</p>
    <p class="abs teacher-name">HENRIKE BOLT</p>
    <p class="abs teacher-role">Zertifizierte Yogalehrerin/Yogatherapeutin</p>

    <div class="field" style="top:267px"><span>Name</span></div>
    <div class="field" style="top:302px"><span>Strasse</span><span>PLZ</span></div>
    <div class="field" style="top:337px"><span>Ort</span><span>Telefon</span></div>
    <div class="field" style="top:372px"><span>E-Mail</span></div>

    <div class="abs divider"></div>
    <div class="abs stamp">BITTE<br>FRANKIEREN</div>
    <address class="abs address" style="font-style:normal">Atemfluss<br>Henrike Bolt<br>Lindenweg 12<br>8460 Feldbach</address>
  </section>

</main>
</body>
</html>
```